Lone Mesa Haulworks Garage web site for repairs,Parts, Accessories and Off Road

Need a wed site design for our light duty truck repair shop, also need to be able to sell our products from this page as well. Has our logo as the headliner and brief description of what we do and our history. An example of what we would want it to work like can be seen at www.garvinsfuelworks.example . This is a good example of style and accesses ability to buy parts we have.

Target Market(s)

Light duty Diesel truck owners(Brell,Kastor,Vantorine)

Industry/Entity Type

Shop

Number of Pages Required

3 page

Font styles to use
Other font styles liked:
• The same font as our logo

Requirements
Must have
• A little about the shop and all of our services,availability to purchase our products, also a map of where we are located.
Nice to have
• I like the design of www.Garvinsfuelworks.example. Its easy to use and very descriptive of parts available

```html
<!DOCTYPE html>
<html lang="en">
<head>
<meta charset="utf-8">
<title>Lone Mesa Haulworks Garage</title>
<link rel="stylesheet" href="https://fonts.googleapis.com/css2?family=Raleway:wght@400;600;700;800&family=Open+Sans:wght@400;600;700&display=swap">
<style>
:root{
  --navy:#0f2b57;
  --navy-dark:#0a1f40;
  --blue:#1d6fb8;
  --yellow:#f4c20d;
  --gray-bg:#e9e9ea;
  --card:#ffffff;
  --icon-gray:#d7d8da;
  --text:#333840;
  --muted:#7a7f87;
  --footer:#2b2b2c;
  --footer-bar:#1f1f20;
  --footer-text:#b9bcc1;
}
*{box-sizing:border-box;margin:0;padding:0}
html,body{width:1200px;height:2356px;overflow:hidden}
body{font-family:"Open Sans",sans-serif;color:var(--text);background:#fff;position:relative}

/* header */
.site-header{height:112px;background:var(--navy);display:flex;align-items:center;justify-content:space-between;padding:0 64px 0 140px}
.brand{display:flex;align-items:center;gap:12px;font-family:"Raleway",sans-serif;font-weight:800;font-size:26px;color:#fff;letter-spacing:1px;text-transform:uppercase}
.brand-mark{width:14px;height:14px;background:var(--yellow)}
.main-nav{display:flex;height:112px}
.main-nav a{display:flex;align-items:center;padding:0 26px;color:#fff;text-decoration:none;font-family:"Raleway",sans-serif;font-size:14px;font-weight:600;letter-spacing:.5px;border-left:1px solid rgba(255,255,255,.15)}
.main-nav a.active{background:rgba(255,255,255,.14)}

/* hero */
.hero{height:576px;background:#fff;position:relative;text-align:center}
.hero h1{padding-top:36px;font-family:"Raleway",sans-serif;font-weight:700;font-size:28px;line-height:38px;color:var(--blue);text-transform:uppercase;width:720px;margin:0 auto}
.btn{display:inline-block;font-family:"Raleway",sans-serif;font-weight:600;font-size:14px;letter-spacing:1px;text-transform:uppercase;text-decoration:none}
.btn-primary{background:var(--navy);color:#fff;padding:14px 34px;margin-top:22px}
.hero-trucks{position:absolute;top:180px;left:0;right:0;height:360px}
.truck{position:absolute;top:0;height:360px;width:520px;border-radius:8px}
.truck-red{left:20px;background:radial-gradient(ellipse at 45% 45%,#d8262b 0%,#a8161b 45%,rgba(255,255,255,0) 72%)}
.truck-blue{right:20px;background:radial-gradient(ellipse at 55% 45%,#2546c8 0%,#16308f 45%,rgba(255,255,255,0) 72%)}
.slider-dots{position:absolute;bottom:18px;left:0;right:0;display:flex;justify-content:center;gap:12px}
.slider-dots span{width:12px;height:12px;border-radius:50%;background:#c9cbd0}
.slider-dots span.on{background:#8a8e95}

/* promo band */
.promo{height:64px;display:flex;background:var(--navy)}
.promo-accent{width:270px;background:var(--yellow);clip-path:polygon(0 0,100% 0,88% 100%,0 100%)}
.promo-body{flex:1;display:flex;align-items:center;padding-left:10px}
.promo-icon{width:44px;height:44px;border-radius:50%;background:var(--yellow);display:flex;align-items:center;justify-content:center;margin-right:22px}
.promo-text h3{font-family:"Raleway",sans-serif;font-size:17px;font-weight:700;color:#fff;text-transform:uppercase}
.promo-text p{font-size:11px;color:#cdd6e4;text-transform:uppercase;letter-spacing:.5px}
.promo-text p b{color:#fff}
.btn-outline{margin-left:auto;margin-right:260px;border:1px solid #fff;color:#fff;padding:9px 40px;font-size:13px}

/* section titles */
.section-title{display:flex;align-items:center;justify-content:center;gap:18px;font-family:"Raleway",sans-serif;font-size:30px;font-weight:600;color:var(--navy);text-transform:uppercase}
.section-title .rule{display:flex;align-items:center;gap:6px}
.section-title .rule i{display:block;width:60px;height:2px;background:currentColor}
.section-title .rule b{font-weight:400;font-size:26px}

/* services */
.services{background:var(--gray-bg);height:1068px;padding-top:80px}
.service-grid{display:grid;grid-template-columns:468px 468px;gap:40px 64px;justify-content:center;margin-top:62px}
.service-card{height:132px;background:var(--card);display:flex;box-shadow:0 2px 6px rgba(0,0,0,.08)}
.service-icon{width:130px;background:var(--icon-gray);display:flex;align-items:center;justify-content:center;clip-path:polygon(0 0,100% 0,82% 100%,0 100%);padding-right:18px}
.service-icon.featured{background:var(--navy)}
.service-info{padding:26px 22px 0 20px}
.service-info h4{font-family:"Raleway",sans-serif;font-weight:700;font-size:16px;color:var(--navy);text-transform:uppercase;margin-bottom:8px}
.service-info p{font-size:11.5px;line-height:17px;color:var(--muted)}

.products-title{margin-top:100px}
.product-grid{display:grid;grid-template-columns:repeat(4,232px);gap:26px;justify-content:center;margin-top:60px}
.product{background:#fff;box-shadow:0 2px 8px rgba(0,0,0,.12)}
.product-photo{height:290px;background:radial-gradient(circle at 50% 50%,#c3c6cb 0%,#e8e9eb 45%,#fff 75%)}
.product-label{height:62px;background:var(--navy);color:#fff;text-align:center;padding-top:12px}
.product-label h5{font-size:13px;font-weight:700}
.product-label p{font-size:12px;color:#d5dbe6}

/* contact */
.contact{background:var(--footer);height:480px;padding-top:52px;color:var(--footer-text)}
.contact .section-title{color:#fff;font-weight:500}
.contact-intro{width:540px;margin:18px auto 0;text-align:center;font-size:13px;line-height:20px}
.contact-body{display:flex;padding:48px 0 0 100px}
.contact-form{width:616px;display:grid;grid-template-columns:1fr 1fr;gap:12px 16px}
.field{border:1px solid #5a5a5c;height:30px;font-size:11px;padding:7px 10px;color:#9a9da2}
.field.message{grid-column:1 / 3;height:132px}
.btn-send{grid-column:1 / 2;width:96px;height:32px;background:var(--navy);color:#fff;display:flex;align-items:center;justify-content:center;margin-top:14px;font-size:13px}
.contact-info{margin-left:104px;list-style:none;font-size:12px;line-height:17px}
.contact-info li{display:flex;gap:14px;margin-bottom:14px;color:#e1e3e6}
.contact-info svg{flex:none;margin-top:1px}
.social{display:flex;gap:14px;margin:24px 0 0 90px}
.social span{width:26px;height:26px;border-radius:50%;background:#fff}

.footer-bar{height:56px;background:var(--footer-bar);display:flex;align-items:center;justify-content:center;position:relative;font-size:12px;color:#8d9096}
.to-top{position:absolute;right:64px;top:16px;width:24px;height:24px;border:1px solid #6a6d72;display:flex;align-items:center;justify-content:center}
</style>
</head>
<body>

<header class="site-header">
  <div class="brand"><span class="brand-mark"></span>Lone Mesa</div>
  <nav class="main-nav">
    <a class="active" href="#">HOME</a>
    <a href="#">OUR TRUCKS</a>
    <a href="#">SPECIAL OFFERS</a>
    <a href="#">SERVICES</a>
    <a href="#">BLOG</a>
    <a href="#">CONTACT</a>
  </nav>
</header>

<section class="hero">
  <h1>Perspiciatis unde omnis iste natus error sit voluptatem accusantium doloremque</h1>
  <a class="btn btn-primary" href="#">Get Started</a>
  <div class="hero-trucks">
    <div class="truck truck-red" role="img" aria-label="Red semi truck cab, three-quarter front view"></div>
    <div class="truck truck-blue" role="img" aria-label="Blue semi truck cab, three-quarter front view"></div>
  </div>
  <div class="slider-dots"><span class="on"></span><span></span><span></span></div>
</section>

<section class="promo">
  <div class="promo-accent"></div>
  <div class="promo-body">
    <div class="promo-icon">
      <svg width="24" height="24" viewBox="0 0 24 24"><circle cx="12" cy="12" r="7" fill="none" stroke="#0f2b57" stroke-width="3"/><circle cx="12" cy="12" r="2.5" fill="#0f2b57"/></svg>
    </div>
    <div class="promo-text">
      <h3>Save your money</h3>
      <p>With special auto service <b>discounts</b> and <b>benefits</b></p>
    </div>
    <a class="btn btn-outline" href="#">Get Now</a>
  </div>
</section>

<section class="services">
  <h2 class="section-title"><span class="rule"><i></i><b>//</b></span>Our Services<span class="rule"><b>//</b><i></i></span></h2>
  <div class="service-grid">
    <article class="service-card">
      <div class="service-icon">
        <svg width="52" height="52" viewBox="0 0 52 52"><circle cx="26" cy="26" r="24" fill="#0f2b57"/><path d="M17 35l12-12m0 0a6 6 0 1 0 4-8l-3 3 2 2 3-3a6 6 0 0 1-6 6" fill="none" stroke="#fff" stroke-width="3" stroke-linecap="round"/></svg>
      </div>
      <div class="service-info"><h4>Truck Repair</h4><p>Complete diesel diagnostics and repair for light duty trucks, done right by certified techs with fair pricing.</p></div>
    </article>
    <article class="service-card">
      <div class="service-icon">
        <svg width="52" height="40" viewBox="0 0 52 40"><rect x="2" y="8" width="30" height="20" fill="#0f2b57"/><path d="M32 14h10l8 8v6H32z" fill="#0f2b57"/><circle cx="12" cy="32" r="5" fill="#0f2b57" stroke="#d7d8da" stroke-width="2"/><circle cx="40" cy="32" r="5" fill="#0f2b57" stroke="#d7d8da" stroke-width="2"/></svg>
      </div>
      <div class="service-info"><h4>Truck Repair</h4><p>Complete diesel diagnostics and repair for light duty trucks, done right by certified techs with fair pricing.</p></div>
    </article>
    <article class="service-card">
      <div class="service-icon featured">
        <svg width="52" height="40" viewBox="0 0 52 40"><rect x="2" y="8" width="30" height="20" fill="#f4c20d"/><path d="M32 14h10l8 8v6H32z" fill="#f4c20d"/><circle cx="12" cy="32" r="5" fill="#f4c20d" stroke="#0f2b57" stroke-width="2"/><circle cx="40" cy="32" r="5" fill="#f4c20d" stroke="#0f2b57" stroke-width="2"/></svg>
      </div>
      <div class="service-info"><h4>Truck Repair</h4><p>Complete diesel diagnostics and repair for light duty trucks, done right by certified techs with fair pricing.</p></div>
    </article>
    <article class="service-card">
      <div class="service-icon">
        <svg width="52" height="52" viewBox="0 0 52 52"><circle cx="26" cy="26" r="24" fill="#0f2b57"/><rect x="12" y="20" width="18" height="12" fill="#fff"/><path d="M30 23h6l5 5v4H30z" fill="#fff"/><circle cx="18" cy="35" r="3" fill="#fff"/><circle cx="35" cy="35" r="3" fill="#fff"/></svg>
      </div>
      <div class="service-info"><h4>Truck Repair</h4><p>Complete diesel diagnostics and repair for light duty trucks, done right by certified techs with fair pricing.</p></div>
    </article>
  </div>

  <h2 class="section-title products-title"><span class="rule"><i></i><b>//</b></span>Our Products<span class="rule"><b>//</b><i></i></span></h2>
  <div class="product-grid">
    <article class="product">
      <div class="product-photo" role="img" aria-label="Engine pistons with connecting rods"></div>
      <div class="product-label"><h5>Kastor Torvane 5.9L 2003</h5><p>Price: $200.00</p></div>
    </article>
    <article class="product">
      <div class="product-photo" role="img" aria-label="Set of engine pistons on a crankshaft"></div>
      <div class="product-label"><h5>Kastor Torvane 5.9L 2003</h5><p>Price: $200.00</p></div>
    </article>
    <article class="product">
      <div class="product-photo" role="img" aria-label="Assorted oil and fuel filters"></div>
      <div class="product-label"><h5>Kastor Torvane 5.9L 2003</h5><p>Price: $200.00</p></div>
    </article>
    <article class="product">
      <div class="product-photo" role="img" aria-label="Row of spark plugs"></div>
      <div class="product-label"><h5>Kastor Torvane 5.9L 2003</h5><p>Price: $200.00</p></div>
    </article>
  </div>
</section>

<section class="contact">
  <h2 class="section-title"><span class="rule"><i></i><b>//</b></span>Contact Us<span class="rule"><b>//</b><i></i></span></h2>
  <p class="contact-intro">Stop by the shop or send us a note below and our team will get back to you within one business day.</p>
  <div class="contact-body">
    <div class="contact-form">
      <div class="field">Name</div>
      <div class="field">Email</div>
      <div class="field message">Message</div>
      <div class="btn-send">SEND</div>
    </div>
    <div>
      <ul class="contact-info">
        <li><svg width="14" height="14" viewBox="0 0 14 14"><path d="M3 1l2.5 3-1.5 1.5a8 8 0 0 0 4.5 4.5L10 8.5 13 11l-1.5 2C6 13 1 8 1 2.5z" fill="#fff"/></svg>TEL: +1 (915) 555 0140</li>
        <li><svg width="14" height="14" viewBox="0 0 14 14"><path d="M7 1a4.5 4.5 0 0 1 4.5 4.5C11.5 9 7 13 7 13S2.5 9 2.5 5.5A4.5 4.5 0 0 1 7 1z" fill="#fff"/><circle cx="7" cy="5.5" r="1.6" fill="#2b2b2c"/></svg><span>1420 MESA RIDGE RD, SUITE 8<br>LONE MESA, TX 79000, UNITED STATES</span></li>
        <li><svg width="14" height="14" viewBox="0 0 14 14"><rect x="1" y="3" width="12" height="8" fill="#fff"/><path d="M1 3l6 5 6-5" fill="none" stroke="#2b2b2c" stroke-width="1.2"/></svg>info@garvinsfuelworks.example</li>
        <li><svg width="14" height="14" viewBox="0 0 14 14"><circle cx="7" cy="7" r="5.5" fill="none" stroke="#fff" stroke-width="1.4"/><path d="M1.5 7h11M7 1.5c-3 3.5-3 7.5 0 11M7 1.5c3 3.5 3 7.5 0 11" fill="none" stroke="#fff" stroke-width="1"/></svg>www.garvinsfuelworks.example</li>
      </ul>
      <div class="social"><span></span><span></span><span></span></div>
    </div>
  </div>
</section>

<footer class="footer-bar">
  © 2015 Lone Mesa All Rights Reserved
  <span class="to-top"><svg width="10" height="10" viewBox="0 0 10 10"><path d="M1 7l4-4 4 4" fill="none" stroke="#b9bcc1" stroke-width="1.5"/></svg></span>
</footer>

</body>
</html>
```